依頼詳細
ターゲットの幅が広いため、まずは人向けの大人から子供までを対象としたいと考えています。
商品名は善玉発酵ミスト 「ふもれ」とし、150ml程度のスプレーボトルに貼り付ける商品シール、それとスプレーボトルを入れる箱の作成依頼をお願いしたいと考えています。
ボトルの色は今後の決定になりますが、白、青のどちらかとなります。
出来るだけ万人に対応できるような商品シールの作成をご提案頂きたいです。
終了後、商品ケース(箱)なども提案依頼をお願いするほか、ターゲットを変えて販売する予定のためよろしくお願いします。

```html
<!DOCTYPE html>
<html lang="ja">
<head>
<meta charset="utf-8">
<title>善玉発酵ミスト ふもれ ラベル・パッケージ</title>
<link rel="stylesheet" href="https://fonts.googleapis.com/css2?family=M+PLUS+Rounded+1c:wght@400;700;800&family=Noto+Sans+JP:wght@500;700;900&display=swap">
<style>
  :root {
    --brand-blue: #233f9a;
    --paper: #ffffff;
    --stage: #eceef2;
    --face-tone: #dfe5f4;
  }
  * { margin: 0; padding: 0; box-sizing: border-box; }
  html, body { width: 876px; height: 1200px; overflow: hidden; }
  body {
    background: var(--stage);
    font-family: "Noto Sans JP", sans-serif;
    color: var(--brand-blue);
    position: relative;
  }
  .label, .box-front {
    position: absolute;
    background: var(--paper);
    display: flex;
    flex-direction: column;
    align-items: center;
    box-shadow: 0 2px 10px rgba(0,0,0,0.08);
    overflow: hidden;
  }
  .label { left: 60px; top: 250px; width: 340px; height: 700px; }
  .box-front { left: 460px; top: 100px; width: 356px; height: 1000px; }

  .box-top { width: 100%; height: 150px; background: var(--brand-blue); }
  .box-bottom {
    margin-top: auto; width: 100%; height: 190px; background: var(--brand-blue);
    display: flex; align-items: flex-end; justify-content: flex-end; padding: 0 22px 20px;
  }
  .made-in { color: var(--paper); font-size: 13px; letter-spacing: 0.12em; font-weight: 500; }

  .series {
    font-weight: 900; text-align: center; line-height: 1.25;
    font-size: 30px; letter-spacing: 0.06em;
  }
  .series .bullet { font-size: 0.6em; vertical-align: middle; margin-right: 4px; }
  .product-name {
    font-family: "M PLUS Rounded 1c", sans-serif; font-weight: 400;
    letter-spacing: 0.04em; line-height: 1; white-space: nowrap;
  }
  .character-art {
    border-radius: 50%/45%;
    background: radial-gradient(circle at 50% 45%, var(--face-tone), #c7d1ec);
  }
  .badge { display: flex; flex-direction: column; align-items: center; gap: 4px; }
  .badge-pill {
    background: var(--brand-blue); color: var(--paper); font-weight: 700;
    border-radius: 999px; font-size: 13px; padding: 2px 12px; letter-spacing: 0.08em;
  }
  .badge-note { font-size: 13px; font-weight: 700; letter-spacing: 0.2em; }
  .ingredient {
    font-weight: 900; font-size: 30px; letter-spacing: 0.3em; line-height: 1;
    padding-left: 0.3em;
  }
  .ingredient-type { font-weight: 700; font-size: 16px; letter-spacing: 0.15em; margin-top: 8px; }

  .label .series { margin-top: 48px; }
  .label .product-name { margin-top: 34px; font-size: 78px; }
  .label .character-art { width: 170px; height: 110px; margin-top: 34px; }
  .label .badge { margin-top: 26px; }
  .label .ingredient { margin-top: 32px; }
  .label-base { margin-top: auto; width: 100%; height: 90px; background: var(--brand-blue); }

  .box-front .series { margin-top: 48px; }
  .box-front .product-name { margin-top: 46px; font-size: 88px; }
  .box-front .character-art { width: 180px; height: 112px; margin-top: 42px; }
  .box-front .badge { margin-top: 30px; }
  .box-front .ingredient { margin-top: 42px; }
</style>
</head>
<body>
  <section class="label" aria-label="ボトルラベル">
    <h1 class="series"><span class="bullet">●</span>善玉発酵<br>ミスト</h1>
    <p class="product-name">ふもれ</p>
    <div class="character-art" role="img" aria-label="大人と子どものキャラクターイラスト"></div>
    <div class="badge">
      <span class="badge-pill">管理栄養士 医学博士</span>
      <span class="badge-note">共同開発</span>
    </div>
    <p class="ingredient">乳酸菌</p>
    <p class="ingredient-type">ローション</p>
    <div class="label-base"></div>
  </section>

  <section class="box-front" aria-label="パッケージ正面">
    <div class="box-top"></div>
    <h2 class="series"><span class="bullet">●</span>善玉発酵<br>ミスト</h2>
    <p class="product-name">ふもれ</p>
    <div class="character-art" role="img" aria-label="大人と子どものキャラクターイラスト"></div>
    <div class="badge">
      <span class="badge-pill">管理栄養士 医学博士</span>
      <span class="badge-note">共同開発</span>
    </div>
    <p class="ingredient">乳酸菌</p>
    <p class="ingredient-type">ローション</p>
    <div class="box-bottom"><span class="made-in">MADE IN JAPAN</span></div>
  </section>
</body>
</html>
```